Condersing Gas Boiler Upgrade and Heating Controls Flyer

We need a 2 page brochure designed for a Renewable Energy installer. This brochure will be sent to home owners but also available in our showroom. We do not want the brochure to be too technical but still provide information. We want to use on the brochure:

First Page
- Brightfern Renewable Logo
- Korbalt Gas Boiler Logo and picture of boiler
- Grants of up to €1221 available
- 5 year warranty on parts and labour
- Benefits of upgrading to a condensing gas boiler

Second Page
- Picture attached
- Save up to 40% on heating bills
- Benefits of heating controls upgrade

Target Market(s)

Home Owners

Industry/Entity Type

Oil And Gas

Logo Text

Brightfern Renewable Energy

Font styles to use
Sans Serif

Colors
cadf82
abd036
9bcb3c

Requirements
Must have
• - Brightfern Renewable Logo
• - Korbalt Gas Boiler Logo and picture of boiler
• - Grants of up to €1221 available
• - Benefits of both upgrading gas boiler and heating controls
• - address and contact details
• - website address - www.brightfern-example.ie
Nice to have
• - green colour throughout

```html
<!DOCTYPE html>
<html lang="en">
<head>
<meta charset="utf-8">
<title>Brightfern Renewable Energy – Heating Upgrade Flyers</title>
<link href="https://fonts.googleapis.com/css2?family=Source+Sans+3:wght@400;600;700&display=swap" rel="stylesheet">
<style>
  :root{
    --bg:#e6e6e4;
    --paper:#ffffff;
    --green-light:#abd26a;
    --green-band:#9bcb3c;
    --green-footer:#8cbb3a;
    --green-text:#7ab32e;
    --green-dark:#2f8a3a;
    --brand-red:#d4262c;
    --white:#ffffff;
  }
  *{box-sizing:border-box;margin:0;padding:0}
  html,body{width:1200px;height:852px;overflow:hidden}
  body{background:var(--bg);font-family:"Source Sans 3",Arial,sans-serif;position:relative}

  .page{position:absolute;top:75px;width:495px;height:702px;background:var(--paper);overflow:hidden;box-shadow:0 2px 8px rgba(0,0,0,.18)}
  .page--boiler{left:71px}
  .page--controls{left:634px}

  .hero{position:absolute;left:0;top:0;width:495px;height:340px}

  .benefits{position:absolute;left:271px;top:300px;width:214px;height:304px;background:var(--green-light);border-radius:0 0 12px 12px;padding:50px 10px 0 10px;color:var(--white)}
  .brand{position:absolute;top:-2px;left:0;right:0;display:flex;align-items:center;justify-content:center;gap:6px;color:var(--green-dark);font-weight:600;font-size:30px;letter-spacing:-.5px}
  .brand-dot{width:20px;height:20px;border-radius:50%;background:var(--green-dark)}
  .benefits h2{font-size:13px;font-weight:600;text-align:center;line-height:1.45;text-transform:uppercase;margin-bottom:8px}
  .benefit-list{list-style:none}
  .benefit-list li{position:relative;padding-left:16px;font-size:11px;line-height:1.05;margin-bottom:10px}
  .benefit-list li svg{position:absolute;left:0;top:0;width:11px;height:11px}

  .boiler-image{position:absolute;left:30px;top:170px;width:170px;height:262px;border-radius:3px;background:linear-gradient(90deg,#f4f4f4,#ffffff 40%,#e4e4e4);box-shadow:2px 3px 6px rgba(0,0,0,.2)}

  .offer{position:absolute;left:20px;top:472px;color:var(--green-text)}
  .offer h1{font-size:21px;font-weight:400;margin-bottom:8px}
  .offer-list{list-style:none}
  .offer-list li{font-size:14px;line-height:1;margin-bottom:8px;display:flex;align-items:center;gap:8px;color:#5ea51e}
  .offer-list svg{width:9px;height:9px}
  .partner{position:absolute;left:20px;top:572px;color:var(--brand-red);font-weight:700;font-size:17px;letter-spacing:1px}

  .phone-image{position:absolute;left:66px;top:184px;width:121px;height:250px;border-radius:12px;background:linear-gradient(180deg,#2b2b2b,#151515 60%,#3a3a3a)}
  .pitch{position:absolute;left:0;width:305px;text-align:center;color:var(--green-text)}
  .pitch--control{top:462px;font-size:19px;line-height:1.3}
  .pitch--save{top:527px;font-size:24px;color:var(--green-dark);line-height:1.1}
  .pitch--save .big{font-size:38px}
  .pitch--bills{top:569px;font-size:24px;color:var(--green-dark)}

  .footer{position:absolute;left:0;bottom:0;width:495px;height:90px}
  .footer-text{position:absolute;left:0;right:0;bottom:10px;text-align:center;color:var(--white)}
  .footer-text .web{font-size:19px;margin-bottom:4px}
  .footer-text .contact{font-size:13px}
</style>
</head>
<body>

<svg width="0" height="0" style="position:absolute">
  <defs>
    <symbol id="bullet-arrow" viewBox="0 0 12 12">
      <circle cx="6" cy="6" r="6" fill="#ffffff"/>
      <path d="M5 3.5 L7.5 6 L5 8.5" fill="none" stroke="#9bcb3c" stroke-width="1.6"/>
    </symbol>
    <symbol id="tick" viewBox="0 0 10 10">
      <path d="M1 5 L4 8 L9 2" fill="none" stroke="#7ab32e" stroke-width="1.6"/>
    </symbol>
  </defs>
</svg>

<!-- Page 1: Gas boiler upgrade -->
<section class="page page--boiler">
  <svg class="hero" viewBox="0 0 495 340">
    <defs>
      <linearGradient id="kitchenTone" x1="0" y1="0" x2="1" y2="1">
        <stop offset="0" stop-color="#c8c4ba"/>
        <stop offset=".5" stop-color="#ece9e3"/>
        <stop offset="1" stop-color="#b9a58a"/>
      </linearGradient>
    </defs>
    <path role="img" aria-label="Photo of a mother cooking and a young girl drawing on the floor of a bright modern kitchen" d="M0 0 H495 V258 C400 300 300 330 200 300 C130 280 60 265 0 268 Z" fill="url(#kitchenTone)"/>
    <path d="M0 268 C60 265 130 280 200 300 C300 330 400 300 495 258 V300 C400 350 280 360 200 332 C130 306 60 280 0 276 Z" fill="var(--green-band)"/>
  </svg>

  <div class="boiler-image" role="img" aria-label="Photo of a white wall-mounted condensing gas boiler"></div>

  <div class="benefits">
    <div class="brand"><span class="brand-dot"></span>Brightfern</div>
    <h2>Benefits of upgrading to a condensing gas boiler</h2>
    <ul class="benefit-list">
      <li><svg><use href="#bullet-arrow"/></svg>Energy saving outdoor temperature sensor standard</li>
      <li><svg><use href="#bullet-arrow"/></svg>Easy installation and service</li>
      <li><svg><use href="#bullet-arrow"/></svg>Low-emission combustion for environmentally-friendly operation</li>
      <li><svg><use href="#bullet-arrow"/></svg>Supply reliability</li>
      <li><svg><use href="#bullet-arrow"/></svg>Simple controls</li>
      <li><svg><use href="#bullet-arrow"/></svg>Space savings</li>
    </ul>
  </div>

  <div class="offer">
    <h1>Gas Boiler Upgrade</h1>
    <ul class="offer-list">
      <li><svg><use href="#tick"/></svg>Grants of up to €1221 available</li>
      <li><svg><use href="#tick"/></svg>5 year warranty on parts and labour</li>
    </ul>
  </div>
  <div class="partner">KORBALT</div>

  <svg class="footer" viewBox="0 0 495 90" preserveAspectRatio="none">
    <path d="M0 30 C150 0 350 0 495 30 V40 C350 12 150 12 0 40 Z" fill="var(--green-light)"/>
    <path d="M0 40 C150 12 350 12 495 40 V90 H0 Z" fill="var(--green-footer)"/>
  </svg>
  <div class="footer-text">
    <div class="web">www.brightfern-example.ie</div>
    <div class="contact">Oakmere Business Park, Glenwood, Co. Dublin, &nbsp;| &nbsp;+(353) (01) 555 0142</div>
  </div>
</section>

<!-- Page 2: Heating controls upgrade -->
<section class="page page--controls">
  <svg class="hero" viewBox="0 0 495 340">
    <defs>
      <linearGradient id="livingTone" x1="0" y1="0" x2="1" y2="1">
        <stop offset="0" stop-color="#dcdcd8"/>
        <stop offset=".55" stop-color="#c9c2bd"/>
        <stop offset="1" stop-color="#6e5a5a"/>
      </linearGradient>
    </defs>
    <path role="img" aria-label="Photo of a modern living room with white sofa, wall shelves and orange accents" d="M0 0 H495 V258 C400 300 300 330 200 300 C130 280 60 265 0 268 Z" fill="url(#livingTone)"/>
    <path d="M0 268 C60 265 130 280 200 300 C300 330 400 300 495 258 V300 C400 350 280 360 200 332 C130 306 60 280 0 276 Z" fill="var(--green-band)"/>
  </svg>

  <div class="phone-image" role="img" aria-label="Smartphone showing a heating control app with room temperature dials"></div>

  <p class="pitch pitch--control">Total control of your<br>heating system – Anywhere!</p>
  <p class="pitch pitch--save">Save up to <span class="big">40%</span></p>
  <p class="pitch pitch--bills">on heating bills</p>

  <div class="benefits">
    <div class="brand"><span class="brand-dot"></span>Brightfern</div>
    <h2>Benefits of heating controls upgrade</h2>
    <ul class="benefit-list">
      <li><svg><use href="#bullet-arrow"/></svg>Easy control your heating system</li>
      <li><svg><use href="#bullet-arrow"/></svg>Activate your heating system en route!</li>
      <li><svg><use href="#bullet-arrow"/></svg>Reduce your energy bills with total control</li>
      <li><svg><use href="#bullet-arrow"/></svg>Control multiple homes at the touch of a button via your smartphone.</li>
    </ul>
  </div>

  <svg class="footer" viewBox="0 0 495 90" preserveAspectRatio="none">
    <path d="M0 30 C150 0 350 0 495 30 V40 C350 12 150 12 0 40 Z" fill="var(--green-light)"/>
    <path d="M0 40 C150 12 350 12 495 40 V90 H0 Z" fill="var(--green-footer)"/>
  </svg>
  <div class="footer-text">
    <div class="web">www.brightfern-example.ie</div>
    <div class="contact">Oakmere Business Park, Glenwood, Co. Dublin, &nbsp;| &nbsp;+(353) (01) 555 0142</div>
  </div>
</section>

</body>
</html>
```